we can communicate on this, but i want to follow the approach we took on Pell|Quorn & Tillet but i feel the card front needs the black background and the platinum and gold logo. The back? I am open. we can use the same info from PQ&T. Vellum Crest is an enhanced equity investment fund - basically a very exclusive boutique hedge fund that uses only stock options. very advanced things. hope you are interested

Contact Information for Business Card

Dr. Owen T. Brisket, CFA
Scientifique de fusée financière
555.014.2296
TheDoc4793@mailvessel.example

4718 Fennel Brook Way N.
West Fargo, ND 58078

No web site

Colors

Designer to choose colors to be used in the design.

Requirements
Nice to have
• I tend to prefer the most visible applications of the logo to include logo and name, the logo version with a black background and the gold and platinum components separated by the black. I see this working well for a single side (logo and name - this is card front to me).
• I am fairly open to other treatments on the reverse side with the data. To me, it makes sense to have a different color rendition of the logo on the reverse and it may be a muted black tone on tone or an oversized portion that would have spot UV. Or, the reverse may play with colors and layout
Should not have
• Other colors = no no
• Decorative font

```html
<!DOCTYPE html>
<html lang="fr">
<head>
<meta charset="utf-8">
<title>Vellum Crest — Business Card</title>
<link rel="stylesheet" href="https://fonts.googleapis.com/css2?family=Lato:wght@400;700&family=Montserrat:wght@700&display=swap">
<style>
  :root {
    --backdrop: #5f5954;
    --paper: #f6f6f6;
    --paper-shade: #e4e4e4;
    --ink: #0d0e10;
    --gold: #c39a2b;
    --gold-deep: #a37a1c;
    --divider: #c8772f;
    --text-grey: #4a4a4a;
    --white: #f2f2f2;
  }
  * { margin: 0; padding: 0; box-sizing: border-box; }
  html, body {
    width: 1200px; height: 900px; overflow: hidden;
    background: var(--backdrop);
  }
  .canvas { position: relative; width: 1200px; height: 900px; }

  .card {
    position: absolute;
    width: 580px; height: 332px;
    border-left: 6px solid var(--gold);
    border-bottom: 6px solid var(--gold);
    box-shadow: 0 18px 36px rgba(0,0,0,0.45);
  }

  /* Info side */
  .card--info {
    left: 70px; top: 90px;
    background: linear-gradient(180deg, var(--paper-shade), var(--paper));
    display: flex; align-items: center;
    padding: 0 28px 0 36px;
  }
  .brand {
    display: flex; flex-direction: column; align-items: center;
    width: 190px; flex: none;
  }
  .brand__dot {
    width: 64px; height: 64px; border-radius: 50%;
    background: var(--gold);
    margin-bottom: 16px;
  }
  .brand__name {
    font-family: "Montserrat", sans-serif; font-weight: 700;
    font-size: 21px; letter-spacing: 1px; text-transform: uppercase;
    color: var(--ink); text-align: center; line-height: 1.15;
  }
  .divider {
    width: 1.5px; height: 160px; background: var(--divider);
    margin: 0 24px 0 20px; flex: none;
  }
  .details { font-family: "Lato", sans-serif; min-width: 0; }
  .details__name {
    color: var(--gold-deep); font-weight: 700; font-size: 22px; line-height: 1.1;
    white-space: nowrap;
  }
  .details__name small { font-size: 12px; }
  .details__title {
    color: var(--text-grey); font-weight: 700; font-size: 12.5px; margin: 4px 0 18px;
  }
  .contact { list-style: none; }
  .contact__row {
    display: flex; align-items: flex-start; gap: 12px;
    color: var(--text-grey); font-size: 13.5px; line-height: 1.25;
    margin-bottom: 7px; white-space: nowrap;
  }
  .contact__icon { width: 16px; height: 16px; flex: none; margin-top: 1px; }

  /* Brand side */
  .card--brand {
    left: 550px; top: 478px;
    background: var(--ink);
    display: flex; flex-direction: column; align-items: center; justify-content: center;
  }
  .card--brand .brand__dot { width: 120px; height: 120px; margin-bottom: 26px; }
  .card--brand .brand__name { color: var(--white); font-size: 38px; letter-spacing: 2px; }
</style>
</head>
<body>
<main class="canvas">

  <section class="card card--info">
    <div class="brand">
      <div class="brand__dot"></div>
      <div class="brand__name">Vellum Crest</div>
    </div>
    <div class="divider"></div>
    <div class="details">
      <p class="details__name">Dr. Owen T. Brisket, <small>CFA</small></p>
      <p class="details__title">Scientifique des Fusées Financières</p>
      <ul class="contact">
        <li class="contact__row">
          <svg class="contact__icon" viewBox="0 0 16 16" aria-hidden="true"><path fill="#c39a2b" d="M4.2 1.5l2 3.2-1.3 1.4c.8 1.9 2.3 3.4 4.2 4.2l1.4-1.3 3.2 2-.9 2.6C8 13.2 2.8 8 1.4 2.4z"/></svg>
          <span>555.014.2296</span>
        </li>
        <li class="contact__row">
          <svg class="contact__icon" viewBox="0 0 16 16" aria-hidden="true"><rect x="1" y="3.5" width="14" height="9.5" fill="#c39a2b"/><path d="M1 3.8l7 5 7-5" stroke="#f6f6f6" stroke-width="1.2" fill="none"/></svg>
          <span>TheDoc4793@mailvessel.example</span>
        </li>
        <li class="contact__row">
          <svg class="contact__icon" viewBox="0 0 16 16" aria-hidden="true"><path fill="#c39a2b" d="M8 1a5 5 0 0 0-5 5c0 3.6 5 9 5 9s5-5.4 5-9a5 5 0 0 0-5-5zm0 7a2 2 0 1 1 0-4 2 2 0 0 1 0 4z"/></svg>
          <span>4718 Fennel Brook Way N.<br>West Fargo, ND 58078</span>
        </li>
      </ul>
    </div>
  </section>

  <section class="card card--brand">
    <div class="brand__dot"></div>
    <div class="brand__name">Vellum Crest</div>
  </section>

</main>
</body>
</html>
```